New Customers - Women's Apparel Postcard

We are in the process of buying a mailing list to try to get some new customers. We would like to entice them with a bunch of pictures of our clothing and a lucrative offer. I will attach some examples.
MAIN MESSAGE: We have great fashion for women of all ages & all sizes!
SECONDARY MESSAGE: Try us on, you are gonna love our great fashions:
OFFER: $10.00 off $20.00 purchase

Target Market(s)

45+ women

Industry/Entity Type

Womens Clothing

Requirements
Must have
• strong call to action

```html
<!DOCTYPE html>
<html lang="en">
<head>
<meta charset="utf-8">
<title>Maple Lane – New Customer Postcard</title>
<link href="https://fonts.googleapis.com/css2?family=Della+Respira&display=swap" rel="stylesheet">
<style>
  :root {
    --page-bg: #2a2a2a;
    --card-white: #ffffff;
    --peach-light: #fbf1e6;
    --peach: #f6dcc6;
    --peach-warm: #f3d3b8;
    --accent-red: #e2242b;
    --ink: #1c1a1a;
    --photo-dark: #3a3734;
    --photo-mid: #8a8580;
    --line-grey: #8c8c8c;
  }
  * { margin: 0; padding: 0; box-sizing: border-box; }
  html, body {
    width: 900px; height: 1200px; overflow: hidden;
    background: var(--page-bg);
  }
  .canvas { position: relative; width: 900px; height: 1200px; }
  .postcard {
    position: absolute; left: 68px; width: 762px; height: 494px;
    overflow: hidden;
    background: linear-gradient(135deg, var(--peach-light) 0%, var(--peach) 55%, var(--peach-warm) 100%);
    font-family: "Della Respira", Georgia, serif;
    color: var(--ink);
  }
  .postcard--front { top: 58px; }
  .postcard--back { top: 625px; }
  .card-shape { position: absolute; inset: 0; width: 762px; height: 494px; }

  /* Front */
  .model-photo {
    position: absolute; left: 32px; top: 12px; width: 200px; height: 482px;
    background: linear-gradient(180deg, #e9dfd4 0%, var(--photo-mid) 22%, var(--photo-dark) 55%, #4b3a30 100%);
    border-radius: 90px 90px 20px 20px;
  }
  .brand-name {
    position: absolute; right: 26px; top: 38px;
    font-size: 40px; color: var(--ink); line-height: 1; white-space: nowrap;
  }
  .front-copy {
    position: absolute; right: 22px; top: 162px;
    text-align: right; font-size: 25px; line-height: 38px; white-space: nowrap;
  }
  .front-copy .main-message { margin-bottom: 39px; }
  .front-copy .offer { color: var(--accent-red); }

  /* Back */
  .back-headline {
    position: absolute; left: 40px; top: 30px;
    font-size: 31px; line-height: 46px; font-weight: normal; color: var(--accent-red);
  }
  .back-brand {
    position: absolute; left: 82px; top: 150px; width: 215px;
  }
  .back-brand .brand-name { position: static; font-size: 38px; display: block; }
  .back-brand .web-address {
    display: block; margin-top: 14px; padding-top: 4px;
    border-top: 2px solid var(--ink);
    font-size: 12px; letter-spacing: 1px; white-space: nowrap;
  }
  .store-details {
    position: absolute; left: 40px; top: 286px;
    font-size: 23px; line-height: 34px;
  }
  .store-details .city { margin-right: 26px; }
  .stamp-box {
    position: absolute; left: 643px; top: 43px; width: 93px; height: 112px;
    border: 1px solid var(--line-grey); background: var(--card-white);
  }
  .address-lines {
    position: absolute; left: 529px; top: 190px; width: 214px;
  }
  .address-lines span {
    display: block; height: 25.5px; border-bottom: 1px solid var(--line-grey);
  }
</style>
</head>
<body>
<main class="canvas">

  <section class="postcard postcard--front">
    <svg class="card-shape" viewBox="0 0 762 494" aria-hidden="true">
      <path d="M0 0 H277 Q460 247 250 494 H0 Z" fill="var(--card-white)"/>
      <path d="M277 0 Q460 247 250 494" fill="none" stroke="var(--accent-red)" stroke-width="4"/>
    </svg>
    <div class="model-photo" role="img" aria-label="Photo of a woman wearing a grey knit hooded long cardigan"></div>
    <div class="brand-name">Maple Lane</div>
    <div class="front-copy">
      <p class="main-message">We have great fashion for<br>women of all ages &amp; all sizes!</p>
      <p>Try us on, you are gonna love<br>our great fashions:</p>
      <p class="offer">OFFER: $10.00 off $20.00<br>purchase</p>
    </div>
  </section>

  <section class="postcard postcard--back">
    <svg class="card-shape" viewBox="0 0 762 494" aria-hidden="true">
      <path d="M497 0 Q337 247 517 494 H762 V0 Z" fill="var(--card-white)"/>
      <path d="M497 0 Q337 247 517 494" fill="none" stroke="var(--accent-red)" stroke-width="4"/>
    </svg>
    <h2 class="back-headline">Try us on....<br>You're gonna love us!</h2>
    <div class="back-brand">
      <span class="brand-name">Maple Lane</span>
      <span class="web-address">www.maplelanedirect.com</span>
    </div>
    <div class="store-details">
      <p><span class="city">Fairhaven</span>118 W. Oak St</p>
      <p>555-014-2268</p>
      <p>offer valid at Fairhaven Maple<br>Lane ONLY</p>
    </div>
    <div class="stamp-box"></div>
    <div class="address-lines"><span></span><span></span><span></span><span></span></div>
  </section>

</main>
</body>
</html>
```